Cell phone repair

you can please design me business card

size 3.5" x 2"

colors blue and red

fixit rapid logo (you get from my website fixitrapidco.example )

"We Come To You!

It is very simple! You tell us what phone you have, And we come to fix it."

phone number: 555.248.3906

website: www.fixitrapidco.example

email: info@fixitrapidco.example

```html
<!DOCTYPE html>
<html lang="en">
<head>
<meta charset="utf-8">
<title>Fixit Rapid – Business Card</title>
<link href="https://fonts.googleapis.com/css2?family=Nunito:wght@700&family=Roboto:wght@500;700&family=Roboto+Condensed:wght@700&display=swap" rel="stylesheet">
<style>
  :root {
    --stage: #ecedec;
    --card: #ffffff;
    --brand-blue: #29a9e1;
    --brand-red: #ec1c2e;
    --band-dark: #3f4245;
    --band-mid: #6c6f72;
    --text-light: #ffffff;
    --card-shadow: rgba(0, 0, 0, 0.14);
  }
  * { box-sizing: border-box; margin: 0; padding: 0; }
  html, body { width: 1200px; height: 900px; overflow: hidden; }
  body { background: var(--stage); position: relative; font-family: "Roboto", Arial, sans-serif; }

  .card {
    position: absolute;
    top: 300px;
    width: 516px;
    height: 298px;
    background: var(--card);
    border-radius: 24px;
    box-shadow: 0 0 0 2px var(--card-shadow);
    overflow: hidden;
  }
  .card--front { left: 71px; }
  .card--back { left: 615px; }

  .wordmark {
    position: absolute;
    display: flex;
    align-items: center;
    font-family: "Nunito", sans-serif;
    font-weight: 700;
    color: var(--brand-blue);
    white-space: nowrap;
  }
  .wordmark__dot { border-radius: 50%; background: var(--brand-red); flex: none; }
  .card--front .wordmark { left: 100px; top: 110px; font-size: 36px; gap: 16px; }
  .card--front .wordmark__dot { width: 46px; height: 46px; }
  .card--back .wordmark { left: 34px; top: 42px; font-size: 46px; gap: 20px; }
  .card--back .wordmark__dot { width: 60px; height: 60px; }

  .band { position: absolute; left: 0; top: 0; width: 516px; height: 298px; }

  .tagline {
    position: absolute;
    left: 36px;
    top: 190px;
    font-family: "Roboto Condensed", sans-serif;
    font-weight: 700;
    font-size: 29px;
    letter-spacing: -0.5px;
    color: var(--brand-red);
  }
  .pitch {
    position: absolute;
    left: 38px;
    top: 226px;
    font-size: 12px;
    font-weight: 700;
    line-height: 15.5px;
    color: var(--text-light);
  }
  .contact {
    position: absolute;
    left: 310px;
    top: 226px;
    list-style: none;
    font-size: 12px;
    font-weight: 700;
    line-height: 15.5px;
    color: var(--text-light);
  }
  .contact li { display: flex; align-items: center; gap: 6px; }
  .contact svg { width: 11px; height: 11px; fill: var(--brand-blue); flex: none; }
</style>
</head>
<body>

<section class="card card--front" aria-label="Card front">
  <div class="wordmark"><span class="wordmark__name">Fixit Rapid</span><span class="wordmark__dot"></span></div>
</section>

<section class="card card--back" aria-label="Card back">
  <div class="wordmark"><span class="wordmark__name">Fixit Rapid</span><span class="wordmark__dot"></span></div>

  <svg class="band" viewBox="0 0 516 298" role="img" aria-label="Dark photo of hands repairing a phone circuit board">
    <defs>
      <linearGradient id="bandShade" x1="0" y1="0" x2="1" y2="0.4">
        <stop offset="0" stop-color="var(--band-dark)"/>
        <stop offset="0.45" stop-color="var(--band-mid)"/>
        <stop offset="1" stop-color="var(--band-dark)"/>
      </linearGradient>
    </defs>
    <path d="M0 164 H300 C326 164 330 199 358 199 H516 V298 H0 Z" fill="url(#bandShade)"/>
    <path d="M0 164 H300 C326 164 330 199 358 199 H516" fill="none" stroke="var(--brand-red)" stroke-width="3"/>
  </svg>

  <h2 class="tagline">We Come To You!</h2>
  <p class="pitch">It is very simple!<br>You tell us what phone you have,<br>And we come to fix it.</p>

  <ul class="contact">
    <li><svg viewBox="0 0 24 24" aria-hidden="true"><path d="M6.6 10.8a15.1 15.1 0 0 0 6.6 6.6l2.2-2.2c.3-.3.7-.4 1-.2 1.1.4 2.3.6 3.6.6.6 0 1 .4 1 1V20c0 .6-.4 1-1 1C10.6 21 3 13.4 3 4c0-.6.4-1 1-1h3.5c.6 0 1 .4 1 1 0 1.3.2 2.5.6 3.6.1.3 0 .7-.2 1z"/></svg>555 248 3906</li>
    <li><svg viewBox="0 0 24 24" aria-hidden="true"><path d="M2 5h20v14H2z M2 5l10 8 10-8" /></svg>info@fixitrapidco.example</li>
    <li><svg viewBox="0 0 24 24" aria-hidden="true"><circle cx="12" cy="12" r="10"/></svg>www.fixitrapidco.example</li>
  </ul>
</section>

</body>
</html>
```